Unique Brovek Building Bussiness Card Design

www.brovek.com.au

Please see website for Company profile. We require a design that incorporates our logo colours and is unique in shape and style compared to all other business cards.

www.brovek.com.au

INSPIRE US !!!
Updates

Target Market(s)

Facility managers, Building Managers, Architects

Industry/Entity Type

Business

Contact Information for Business Card

Brovek Property Works
Project Manager
Dalton Pryseworth
0437 916 248
Sales@brovek.com.au

Logo Text

Brovek Property Works

Logo styles of interest
Abstract Logo
Requirements
Nice to have
• Card must show we are an established big business to trust.

```html
<!DOCTYPE html>
<html lang="en">
<head>
<meta charset="utf-8">
<title>Brovek Property Works – Business Card</title>
<link href="https://fonts.googleapis.com/css2?family=Tinos:wght@400;700&display=swap" rel="stylesheet">
<style>
  :root {
    --page: #ffffff;
    --card: #ffffff;
    --blue-dark: #1b5580;
    --blue-mid: #2a6a93;
    --blue-light: #3a7ea3;
    --red: #c0272d;
    --orange: #e8692c;
    --peach: #f0925e;
    --white: #ffffff;
    --ink: #1f4e79;
  }
  html, body {
    margin: 0;
    padding: 0;
    width: 1200px;
    height: 1000px;
    overflow: hidden;
    background: var(--page);
  }
  .business-card {
    position: absolute;
    left: 230px;
    top: 295px;
    width: 740px;
    height: 412px;
    background: var(--card);
    box-shadow: 0 2px 10px rgba(0,0,0,0.35);
    overflow: hidden;
    font-family: "Tinos", "Times New Roman", serif;
  }
  .card-waves {
    position: absolute;
    inset: 0;
  }
  .brand {
    position: absolute;
    left: 170px;
    top: 88px;
    display: flex;
    align-items: center;
    gap: 12px;
  }
  .brand-mark {
    width: 34px;
    height: 34px;
    background: var(--orange);
  }
  .brand-name {
    font-size: 44px;
    font-weight: 700;
    color: var(--ink);
    letter-spacing: 0.5px;
  }
  .call-line {
    position: absolute;
    left: 15px;
    top: 318px;
    font-size: 54px;
    line-height: 1;
    color: var(--peach);
  }
  .call-hours {
    position: absolute;
    left: 238px;
    top: 318px;
    font-size: 48px;
    line-height: 1;
    color: var(--white);
  }
  .call-team {
    position: absolute;
    left: 196px;
    top: 350px;
    font-size: 58px;
    line-height: 1;
    color: var(--peach);
  }
  .phone {
    position: absolute;
    left: 15px;
    top: 372px;
    font-size: 29px;
    line-height: 1;
    color: var(--white);
  }
  .email {
    position: absolute;
    right: 12px;
    top: 374px;
    font-size: 27px;
    line-height: 1;
    color: var(--white);
  }
  .email-label {
    color: var(--peach);
  }
</style>
</head>
<body>
  <div class="business-card">
    <svg class="card-waves" width="740" height="412" viewBox="0 0 740 412">
      <defs>
        <linearGradient id="blueBody" x1="0" y1="0" x2="1" y2="0">
          <stop offset="0" stop-color="#3a7fa3"/>
          <stop offset="0.5" stop-color="#22608d"/>
          <stop offset="1" stop-color="#1a5580"/>
        </linearGradient>
        <linearGradient id="blueHump" x1="0" y1="0" x2="0" y2="1">
          <stop offset="0" stop-color="#3b7fa4"/>
          <stop offset="1" stop-color="#24628e"/>
        </linearGradient>
        <linearGradient id="ribbon" x1="0" y1="0" x2="1" y2="0">
          <stop offset="0" stop-color="#c0272d"/>
          <stop offset="0.5" stop-color="#d9502a"/>
          <stop offset="1" stop-color="#e8692c"/>
        </linearGradient>
      </defs>
      <path class="wave-body" fill="url(#blueBody)"
            d="M0,228 C150,232 300,270 380,305 C470,345 580,380 740,340 L740,412 L0,412 Z"/>
      <path class="wave-hump" fill="url(#blueHump)"
            d="M380,303 C480,270 610,262 740,305 L740,340 C580,380 470,345 380,305 Z"/>
      <path class="wave-ribbon" fill="url(#ribbon)"
            d="M0,199 C150,205 300,260 390,298 C470,332 570,378 740,330 L740,340 C570,380 470,345 380,305 C300,270 150,232 0,228 Z"/>
    </svg>

    <div class="brand">
      <span class="brand-mark"></span>
      <span class="brand-name">Brovek.com.au</span>
    </div>

    <div class="call-line">Call our</div>
    <div class="call-hours">24/7</div>
    <div class="call-team">Team</div>
    <div class="phone">0437-916-248</div>
    <div class="email"><span class="email-label">Email:</span> sales@brovek.com.au</div>
  </div>
</body>
</html>
```